Peltrix – Nimbara Flyer for Brivella (Halvern Travel Corporation)

Overview
Halvern Travel Corporation is launching a series of branded flyers to highlight the features and benefits of our Peltrix platform — our all-in-one corporate travel technology suite.
This first flyer will spotlight Nimbara, our risk management and traveller safety solution, and will be published on Brivella as part of a digital awareness campaign.
⸻
Objective
Create a striking, professional, and modern flyer that communicates how Nimbara enhances the Peltrix platform by ensuring traveller safety, communication, and real-time updates.
The design should feel premium, contemporary, and aligned with Halvern Travel’s luxury corporate identity.
⸻
Target Audience
• Corporate clients and travel decision-makers
• Travel managers, procurement teams, and executive assistants
• Existing Halvern Travel corporate partners on Brivella
⸻
Key Message
Nimbara – Your travellers’ safety, visibility, and communication, all in one place.
Part of Peltrix, Halvern Travel’s integrated corporate travel platform.
⸻
Core Features to Highlight
• 24/7 real-time risk alerts
• Instant traveller identification and tracking by location or timeframe
• Two-way communication between traveller and company
• Integrated with travel itineraries for seamless care
• Supports duty-of-care compliance for corporate travel policies
⸻
Tone & Style
• Sophisticated, trusted, and innovative
• Clean lines, premium feel, and minimal clutter
• Should feel like a Halvern Travel-branded asset — not overly “techy”
• Imagery: travel safety, global maps, communication lines, or business travellers in motion
⸻
Design Direction
• Brand: Use Halvern Travel brand colours (gold, charcoal, white, navy)
• Typography: Professional, modern sans-serif fonts
• Logo: Include Halvern Travel and Peltrix logos (can supply if needed)
• CTA: “Discover Nimbara on Peltrix” or “Raise the Halvern Benchmark for Business Trips”
• Layout: Ideal for Brivella post format (square or 4:5 vertical)
⸻
Deliverables
• Editable design file (AI / PSD / InDesign)
• Final exports for social media:
• 1080x1080 px (Brivella square)
• 1080x1350 px (Brivella portrait)
• Include space for light text overlay (for post captioning later)
⸻
Inspiration
• Style similar to luxury tech or premium corporate innovation brands
• Feel: clean, high-contrast, aspirational, minimal

```html
<!DOCTYPE html>
<html lang="en">
<head>
<meta charset="utf-8">
<title>Nimbara on Peltrix – Halvern Travel Flyer</title>
<link rel="stylesheet" href="https://fonts.googleapis.com/css2?family=Poppins:wght@400;500;600;700;800&display=swap">
<style>
  :root {
    --page-bg: #ebebeb;
    --navy-deep: #0f1d44;
    --navy-title: #0c1a3d;
    --sky-top: #9aa6b8;
    --sky-mid: #5b6f91;
    --gold: #dba65f;
    --bronze: #7c5a34;
    --white: #ffffff;
    --screen-light: #eef0f3;
  }
  * { margin: 0; padding: 0; box-sizing: border-box; }
  html, body {
    width: 1200px; height: 2484px; overflow: hidden;
    background: var(--page-bg);
    font-family: "Poppins", sans-serif;
  }
  .flyer {
    position: absolute; left: 107px; top: 749px;
    width: 986px; height: 986px; overflow: hidden;
    color: var(--white);
  }
  .flyer__backdrop {
    position: absolute; inset: 0;
    background:
      radial-gradient(ellipse 60% 40% at 78% 22%, rgba(200,208,222,0.55), transparent 70%),
      radial-gradient(ellipse 45% 25% at 30% 50%, rgba(190,160,130,0.35), transparent 70%),
      linear-gradient(180deg, var(--sky-top) 0%, var(--sky-mid) 32%, #2b3f67 60%, var(--navy-deep) 85%);
  }
  .headline {
    position: absolute; left: 56px; top: 48px;
    font-weight: 700; font-size: 79px; line-height: 67px; letter-spacing: -1px;
  }
  .headline span { display: block; }
  .headline__brand { color: var(--navy-title); }
  .headline__accent { color: var(--gold); }
  .headline__word { color: var(--white); }
  .intro {
    position: absolute; left: 56px; top: 278px; width: 478px;
    font-size: 20.5px; line-height: 25px; text-align: justify; font-weight: 400;
  }
  .intro strong { font-weight: 600; }
  .features {
    position: absolute; left: 56px; top: 495px; list-style: none;
  }
  .features li {
    position: relative; padding-left: 24px;
    font-size: 19px; line-height: 22.5px; font-weight: 500;
    margin-bottom: 22px;
  }
  .features li:nth-child(1) { margin-bottom: 22px; }
  .features svg { position: absolute; left: 0; top: 4px; width: 15px; height: 15px; }
  .cta {
    position: absolute; left: 56px; top: 886px;
    font-size: 27px; line-height: 26px; font-weight: 700; text-transform: uppercase;
  }
  .platform-tab {
    position: absolute; left: 624px; top: 253px; width: 226px; height: 86px;
    background: var(--bronze); border-radius: 24px 24px 0 0;
    text-align: center; padding-top: 16px;
  }
  .platform-tab__name { font-size: 30px; font-weight: 700; line-height: 34px; }
  .platform-tab__org { font-size: 10.5px; font-weight: 500; letter-spacing: 0.3px; }
  .device-showcase {
    position: absolute; left: 558px; top: 338px; width: 322px; height: 222px;
    background: linear-gradient(160deg, var(--screen-light) 0%, #cfd5de 55%, rgba(120,132,150,0.4) 100%);
    clip-path: polygon(20% 0, 80% 0, 80% 12%, 100% 12%, 100% 100%, 0 100%, 0 45%, 20% 45%);
  }
  .traveller-photo {
    position: absolute; left: 503px; top: 568px; width: 441px; height: 440px;
    border-radius: 50% 50% 0 0 / 42% 42% 0 0;
    background:
      radial-gradient(ellipse 40% 35% at 40% 35%, #c9a27a, transparent 70%),
      radial-gradient(ellipse 45% 35% at 70% 70%, #4f7fa6, transparent 70%),
      linear-gradient(135deg, #8a7058 0%, #5a6478 50%, #2c3f5e 100%);
  }
</style>
</head>
<body>
  <main class="flyer">
    <div class="flyer__backdrop" role="img" aria-label="Aircraft wing above clouds at dusk"></div>

    <h1 class="headline">
      <span class="headline__brand">HALVERN</span>
      <span class="headline__accent">TRAVEL’S</span>
      <span class="headline__word">LUXURY</span>
    </h1>

    <p class="intro"><strong>Nimbara</strong> offers 24/7 monitoring making sure you are updated of any issues that occur. With risk alerts, traveller identification and two-way communication the duty of care tool reduces problems with ease.</p>

    <ul class="features">
      <li><svg viewBox="0 0 16 16"><circle cx="8" cy="8" r="6.5" fill="none" stroke="var(--gold)" stroke-width="1.8"/><path d="M5 8.2l2 2 4-4.2" fill="none" stroke="var(--gold)" stroke-width="1.8"/></svg>24/7 Real-Time Risk Alerts</li>
      <li><svg viewBox="0 0 16 16"><circle cx="8" cy="8" r="6.5" fill="none" stroke="var(--gold)" stroke-width="1.8"/><path d="M5 8.2l2 2 4-4.2" fill="none" stroke="var(--gold)" stroke-width="1.8"/></svg>Instant Traveller Identification and<br>Tracking By Location or Timeframe</li>
      <li><svg viewBox="0 0 16 16"><circle cx="8" cy="8" r="6.5" fill="none" stroke="var(--gold)" stroke-width="1.8"/><path d="M5 8.2l2 2 4-4.2" fill="none" stroke="var(--gold)" stroke-width="1.8"/></svg>Two-Way Communication Between<br>Traveller and Company</li>
      <li><svg viewBox="0 0 16 16"><circle cx="8" cy="8" r="6.5" fill="none" stroke="var(--gold)" stroke-width="1.8"/><path d="M5 8.2l2 2 4-4.2" fill="none" stroke="var(--gold)" stroke-width="1.8"/></svg>Integrated with Travel Itineraries for<br>Seamless Care</li>
      <li><svg viewBox="0 0 16 16"><circle cx="8" cy="8" r="6.5" fill="none" stroke="var(--gold)" stroke-width="1.8"/><path d="M5 8.2l2 2 4-4.2" fill="none" stroke="var(--gold)" stroke-width="1.8"/></svg>Supports Duty-of-Care Compliance<br>for Corporate Travel Policies</li>
    </ul>

    <p class="cta">Discover Nimbara<br>on Peltrix</p>

    <div class="platform-tab">
      <div class="platform-tab__name">Peltrix</div>
      <div class="platform-tab__org">HALVERN TRAVEL CORPORATION</div>
    </div>
    <div class="device-showcase" role="img" aria-label="Peltrix dashboard shown on desktop, laptop and phone screens"></div>

    <div class="traveller-photo" role="img" aria-label="Business traveller holding a coffee cup by an aircraft window"></div>
  </main>
</body>
</html>
```